IT Services Business Card Design

We require a business card design for an IT services company called RT Code Transit.

We specialize in taking an organisations software and readying it for deployment to new environments (e.g. Nex 3 to Nex 5). This process is termed application packaging. This is not the same as putting things in boxes but I am happy to use boxes as a pun icon ;-) This is our second step in branding, we currently have a new logo and our poor excuse of a website is next to be updated but it contains information on who we are and what we cover at rtcodetransit.example

We are looking for a fun, modern but stylish and professional looking design.

I have attached the logo in multiple formats including vector formats (and the fonts that created the logo if required)
Updates

Thanks to all the designers so far, some great designs in there.  I will be selecting a card design on the deadline date. 

However, there is still time to submit some more designs.  The majority of the ones I have so far are typical simplistic designs that we have all seen before and I have enough of those to choose from now.  If you wish to submit any more designs, please submit somthing unusual to grab our attention.

Target Market(s)

Project executives of large organisations looking for Nexora migrations

Industry/Entity Type

Software

Requirements
Must have
• Want to show company name, contact name, title, main number, contact number, fax number, email address and website address. I do not want to show the address.
Must use the attached logo, retaining the colours in them.

This has to be a double-sided design. I will be using pelby.example and will be selecting their rounded corner business card design.

Their templates and design requirements (sizing etc.) can be found here: http://uk.pelby.example/help/faq/templates-and-guidelines.html

Happy for company name or website to be on either side of the card.

This design has to be original and not used before for another company

Would like to style it around the business colours in the logo
Nice to have
• Pelby.example has an option for multiple card designs to appear on the back. If this is possible in the budget and time you have and you have a design(s) that work with that but carry the same style and theme, that would be nice to see but not necessary.
Should not have
• We do not want to put a postal address on the cards

```html
<!DOCTYPE html>
<html lang="en">
<head>
<meta charset="utf-8">
<title>RT Code Transit — Business Card</title>
<link rel="stylesheet" href="https://fonts.googleapis.com/css2?family=Libre+Franklin:ital,wght@0,300;0,400;1,300&display=swap">
<style>
  :root {
    --stage: #0e0e0e;
    --card-dark: #2a3029;
    --card-light: #ffffff;
    --ink-white: #ffffff;
    --ink-soft: #d6dad6;
    --ink-title: #b9c8e6;
    --ink-mark: #5a534d;
    --ink-mark-light: #d0d2cf;
    --ink-small: #2b2b2b;
    --brand-blue: #4c7fe0;
  }
  * { box-sizing: border-box; margin: 0; padding: 0; }
  html, body {
    width: 1200px; height: 900px; overflow: hidden;
    background: var(--stage);
    font-family: "Libre Franklin", Arial, sans-serif;
  }
  .canvas { position: relative; width: 1200px; height: 900px; }

  .card {
    position: absolute; left: 368px; width: 449px; height: 268px; overflow: hidden;
  }
  .card--front { top: 133px; background: var(--card-dark); }
  .card--back { top: 452px; background: var(--card-light); }

  .brand {
    display: flex; align-items: center; gap: 10px; font-weight: 300; white-space: nowrap;
  }
  .brand__dot {
    width: 30px; height: 30px; border-radius: 50%; background: var(--brand-blue); flex: none;
  }

  .logo-panel {
    position: absolute; left: 0; top: 75px; width: 220px; height: 111px;
    background: var(--card-light);
    box-shadow: 1px 2px 3px rgba(0,0,0,.55);
    display: flex; align-items: center; justify-content: center;
  }
  .logo-panel .brand { color: var(--ink-mark); font-size: 19px; }

  .contact { position: absolute; left: 240px; top: 97px; color: var(--ink-soft); }
  .contact__name { color: var(--ink-white); font-size: 15px; font-weight: 400; line-height: 20px; }
  .contact__title { color: var(--ink-title); font-size: 11.5px; font-style: italic; font-weight: 300; line-height: 16px; margin-bottom: 1px; }
  .contact__phone { font-size: 11px; font-weight: 300; line-height: 15.5px; }

  .online {
    position: absolute; right: 29px; top: 217px; text-align: right;
    color: var(--ink-white); font-size: 10.5px; font-weight: 300; line-height: 16px;
  }

  .band {
    position: absolute; left: 0; top: 88px; width: 100%; height: 94px;
    background: var(--card-dark);
    box-shadow: 0 1px 2px rgba(0,0,0,.4);
    display: flex; align-items: center; justify-content: center;
  }
  .band .brand { color: var(--ink-mark-light); font-size: 20px; }

  .back-url {
    position: absolute; left: 0; top: 243px; width: 100%; text-align: center;
    color: var(--ink-small); font-size: 8.5px; font-weight: 400;
  }
</style>
</head>
<body>
<main class="canvas">
  <section class="card card--front" aria-label="Card front">
    <div class="logo-panel">
      <div class="brand"><span>RT Code Transit</span><span class="brand__dot"></span></div>
    </div>
    <div class="contact">
      <p class="contact__name">Alan Whitby</p>
      <p class="contact__title">title</p>
      <p class="contact__phone">+22 4100 555 010[main]</p>
      <p class="contact__phone">+22 4100 555 020[contact]</p>
      <p class="contact__phone">+22 4100 555 030[fax]</p>
    </div>
    <div class="online">
      <p>alan.whitby@rtcodetransit.example</p>
      <p>www.rtcodetransit.example</p>
    </div>
  </section>

  <section class="card card--back" aria-label="Card back">
    <div class="band">
      <div class="brand"><span>RT Code Transit</span><span class="brand__dot"></span></div>
    </div>
    <p class="back-url">www.rtcodetransit.example</p>
  </section>
</main>
</body>
</html>
```